Simple web design project

We need a four page web design for a premier domestic cleaning company. We would like to see designs which use white and blue (the blue in the logo - which is attatched). Please could the tab for the pages be horizontal and at the top of the page. Our company logo is attached and should be included on each page. Ideally, we would like the foundations of each page to be the same, with the word content differing as required (word content attatched). Additionally we have attached a flyer which has been distributed to advertise our company. Please could all web designs illustrate the same professional message this flyer does.

Target Market(s)

females with higher than average income, aged 30-50. Have families and work 9-5.

Industry/Entity Type

It Company

Requirements
Must have
• logo on each page. Foundations of each page the same. phone number and email on the bottom of each page.
Should not have
• please no pictures of females cleaning.

```html
<!DOCTYPE html>
<html lang="en">
<head>
<meta charset="utf-8">
<title>Hollowmere Cleaners – Home</title>
<link rel="stylesheet" href="https://fonts.googleapis.com/css2?family=Ubuntu:ital,wght@0,400;0,500;1,500&family=Tinos:wght@400;700&display=swap">
<style>
  :root {
    --page-bg: #f1f1f1;
    --brand-blue: #1d5aa3;
    --nav-dark: #333333;
    --nav-darker: #262626;
    --nav-divider: #505050;
    --active-top: #4aa0ea;
    --active-bottom: #1566c0;
    --text-dark: #1c1c1c;
    --rule: #bdbdbd;
    --footer-bg: #333333;
    --white: #ffffff;
  }
  * { box-sizing: border-box; margin: 0; padding: 0; }
  html, body { width: 1093px; height: 1200px; overflow: hidden; background: var(--page-bg); }
  body { font-family: "Ubuntu", sans-serif; color: var(--text-dark); }
  .page { position: relative; width: 1093px; height: 1200px; overflow: hidden; }

  .brand { position: absolute; left: 33px; top: 26px; display: flex; align-items: center; gap: 10px; }
  .brand-mark { width: 34px; height: 34px; background: var(--brand-blue); }
  .brand-name { font-family: "Tinos", serif; font-size: 30px; color: var(--text-dark); line-height: 1; }
  .brand-tagline { position: absolute; left: 82px; top: 87px; font-family: "Tinos", serif; font-size: 13px; color: var(--text-dark); }

  .contact-strip { position: absolute; right: 38px; top: 70px; font-size: 18px; color: var(--brand-blue); }
  .contact-strip .sep { margin: 0 10px; }

  .main-nav { position: absolute; left: 33px; top: 120px; width: 1020px; height: 66px; border-radius: 11px; overflow: hidden;
    background: linear-gradient(var(--nav-dark), var(--nav-darker)); display: flex; }
  .main-nav a { display: flex; align-items: center; justify-content: center; color: #d8d8d8; text-decoration: none;
    font-size: 19px; font-weight: 500; letter-spacing: 0.3px; border-right: 2px solid var(--nav-divider); }
  .main-nav a.active { color: var(--white); background: radial-gradient(ellipse at 40% 30%, var(--active-top), var(--active-bottom) 75%); }
  .nav-home { width: 221px; }
  .nav-services { width: 224px; }
  .nav-prices { width: 224px; }
  .nav-contact { width: 224px; }
  .nav-spacer { flex: 1; }

  .hero { position: absolute; left: 33px; top: 205px; width: 1020px; height: 430px; border-radius: 9px; overflow: hidden;
    border: 1px solid #c9c9c9; }
  .hero-photo { position: absolute; inset: 0;
    background: linear-gradient(100deg, #6f6863 0%, #b7b1ab 30%, #e4e1dc 50%, #a9a19a 72%, #6e655e 100%); }
  .hero-title { position: absolute; left: 46px; top: 30px; font-size: 63px; font-weight: 500; color: var(--white);
    text-shadow: 2px 3px 4px rgba(0,0,0,0.6); }
  .hero-subtitle { position: absolute; left: 46px; top: 103px; font-size: 25px; color: var(--white);
    text-shadow: 1px 2px 3px rgba(0,0,0,0.7); }

  .section-heading { font-size: 33px; font-weight: 500; font-style: italic; color: var(--brand-blue); }
  .welcome { position: absolute; left: 31px; top: 676px; width: 500px; }
  .welcome p { font-size: 16.5px; line-height: 23px; margin-top: 0; }
  .welcome .section-heading { margin-bottom: 20px; }
  .welcome p + p { margin-top: 23px; }

  .why-us { position: absolute; left: 622px; top: 676px; }
  .why-us .section-heading { margin-bottom: 14px; }
  .why-us ul { list-style: none; }
  .why-us li { display: flex; align-items: center; font-size: 16.5px; height: 23.5px; }
  .why-us svg { width: 20px; height: 18px; margin-right: 10px; margin-left: 3px; }

  .rule { position: absolute; left: 30px; width: 1022px; height: 2px; background: var(--rule); }
  .rule-top { top: 936px; }
  .rule-bottom { top: 1028px; }
  .invite { position: absolute; left: 0; width: 1093px; top: 966px; text-align: center;
    font-size: 26px; font-weight: 500; font-style: italic; color: var(--brand-blue); }

  .site-footer { position: absolute; left: 33px; top: 1096px; width: 1020px; height: 120px; background: var(--footer-bg);
    border-radius: 11px 11px 0 0; color: var(--white); }
  .footer-nav { position: absolute; left: 40px; top: 24px; font-size: 18px; }
  .footer-nav a { color: var(--white); text-decoration: none; }
  .footer-nav .sep { margin: 0 12px; }
  .footer-brand { position: absolute; left: 694px; top: 22px; font-family: "Tinos", serif; font-size: 16px; }
  .footer-brand small { display: block; font-size: 8px; margin-left: 24px; margin-top: 2px; }
  .footer-rights { position: absolute; left: 841px; top: 20px; font-size: 18px; }
</style>
</head>
<body>
<div class="page">
  <header>
    <div class="brand">
      <span class="brand-mark"></span>
      <span class="brand-name">Hollowmere Cleaners</span>
    </div>
    <div class="brand-tagline">Premier Domestic Cleaners</div>
    <div class="contact-strip"><span>07700900461</span><span class="sep">|</span><span>hollowmerecleaners@example.co.uk</span></div>
  </header>

  <nav class="main-nav">
    <a class="nav-home active" href="#">HOME</a>
    <a class="nav-services" href="#">SERVICES</a>
    <a class="nav-prices" href="#">PRICES</a>
    <a class="nav-contact" href="#">CONTACT US</a>
    <span class="nav-spacer"></span>
  </nav>

  <section class="hero">
    <div class="hero-photo" role="img" aria-label="Bright modern living room with a cream corner sofa and a blue bucket of cleaning supplies"></div>
    <h1 class="hero-title">Premium Cleaners</h1>
    <p class="hero-subtitle">We supply quality and tailored cleaning service</p>
  </section>

  <section class="welcome">
    <h2 class="section-heading">Welcome to our website</h2>
    <p>We are a premier domestic cleaning company based in Thornbury Vale, Wessex.</p>
    <p>Our vision is to supply households with a quality, tailored cleaning service, freeing up individuals spare time and replacing the stereo-typical unreliable, inconsistent cleaners.</p>
  </section>

  <section class="why-us">
    <h2 class="section-heading">Why us:</h2>
    <ul>
      <li><svg viewBox="0 0 20 18"><path d="M1 9 L7 15 L19 2" fill="none" stroke="#1c1c1c" stroke-width="3"/></svg>No contracts</li>
      <li><svg viewBox="0 0 20 18"><path d="M1 9 L7 15 L19 2" fill="none" stroke="#1c1c1c" stroke-width="3"/></svg>Insured</li>
      <li><svg viewBox="0 0 20 18"><path d="M1 9 L7 15 L19 2" fill="none" stroke="#1c1c1c" stroke-width="3"/></svg>Free quotes</li>
      <li><svg viewBox="0 0 20 18"><path d="M1 9 L7 15 L19 2" fill="none" stroke="#1c1c1c" stroke-width="3"/></svg>Personalised service</li>
      <li><svg viewBox="0 0 20 18"><path d="M1 9 L7 15 L19 2" fill="none" stroke="#1c1c1c" stroke-width="3"/></svg>We supply all equipment at no extra cost</li>
      <li><svg viewBox="0 0 20 18"><path d="M1 9 L7 15 L19 2" fill="none" stroke="#1c1c1c" stroke-width="3"/></svg>Hassel free service</li>
    </ul>
  </section>

  <div class="rule rule-top"></div>
  <p class="invite">Have a look through our website to see how we can help you.</p>
  <div class="rule rule-bottom"></div>

  <footer class="site-footer">
    <nav class="footer-nav">
      <a href="#">Home</a><span class="sep">|</span><a href="#">Services</a><span class="sep">|</span><a href="#">Prices</a><span class="sep">|</span><a href="#">Contact Us</a>
    </nav>
    <div class="footer-brand">Hollowmere Cleaners<small>Premier Domestic Cleaners</small></div>
    <div class="footer-rights">All Rights Reserved.</div>
  </footer>
</div>
</body>
</html>
```